Seed Company Looking For a Soybean Seed Bag Design

We are are a regional seed company who is currently launching a new line of soybean products. The brand of the product will be Tru-Vora. We are looking for a custom design of a soybean bag measuring 16"x5"x30" (when constructed). We are looking for a modern design that's relatively loud, but not too busy. The proof needs to match with the attached template. We have also provided a proof of a previous bag project (Fox-Brook-Standard) we've done to show how the artwork needs to be laid out. In no way does the new design need to resemble the example. Also attached are some other examples of seed bags.
Agriculture
Designer to choose colors to be used in the design.

```html
<!DOCTYPE html>
<html lang="en">
<head>
<meta charset="utf-8">
<title>Tru-Vora Soybean Seed Bag</title>
<link href="https://fonts.googleapis.com/css2?family=Montserrat:wght@400;600;700&family=Oswald:wght@300;500;700&family=Open+Sans:wght@400;700&display=swap" rel="stylesheet">
<style>
  :root {
    --page: #ffffff;
    --panel: #f4f4f4;
    --fold: #ffffff;
    --green: #2ea44a;
    --lime: #7cb63a;
    --lime-dark: #5f9a2b;
    --grey: #666666;
    --ink: #1a1a1a;
  }
  * { box-sizing: border-box; margin: 0; padding: 0; }
  html, body { width: 1200px; height: 1087px; overflow: hidden; background: var(--page); }
  .canvas { position: relative; width: 1200px; height: 1087px; }
  .bag { position: absolute; left: 17px; top: 18px; width: 1167px; height: 1053px; background: var(--panel); }
  .fold-v, .fold-h { position: absolute; background: var(--fold); }
  .fold-v { top: 18px; width: 2px; height: 1053px; }
  .fold-h { left: 17px; width: 1167px; height: 2px; }

  .illustration { position: absolute; }
  .plant-left { left: 80px; top: 381px; width: 453px; height: 529px;
    background: radial-gradient(ellipse at 50% 45%, rgba(198,221,192,.55), rgba(198,221,192,0) 70%); }
  .plant-right { left: 708px; top: 149px; width: 323px; height: 410px;
    background: radial-gradient(ellipse at 55% 40%, rgba(198,221,192,.6), rgba(198,221,192,0) 70%); }
  .beans { left: 854px; top: 848px; width: 137px; height: 89px; border-radius: 50%;
    background: radial-gradient(ellipse at 45% 45%, #c8d680, #9fb54a 60%, rgba(159,181,74,0) 72%); }

  .brand { position: absolute; text-align: center; }
  .brand-mark { background: var(--green); margin: 0 auto; }
  .brand-name { font-family: 'Montserrat', sans-serif; font-weight: 700; color: var(--green); letter-spacing: 1px; line-height: 1; white-space: nowrap; }
  .brand-left { left: 114px; top: 206px; width: 233px; }
  .brand-left .brand-mark { width: 26px; height: 26px; margin-bottom: 40px; }
  .brand-left .brand-name { font-size: 31px; }
  .brand-right { left: 604px; top: 500px; width: 290px; }
  .brand-right .brand-mark { width: 34px; height: 34px; margin-bottom: 48px; }
  .brand-right .brand-name { font-size: 40px; }

  .info-band { position: absolute; left: 17px; top: 673px; width: 373px; height: 139px; background: var(--green); }
  .info-band::before { content: ""; position: absolute; left: 53px; top: 0; width: 2px; height: 100%; background: var(--fold); }
  .info-band p { position: absolute; left: 91px; top: 26px; width: 272px; font-family: 'Montserrat', sans-serif; font-size: 12.2px; line-height: 16.5px; color: #fff; }

  .badge { position: absolute; width: 114px; height: 114px; border-radius: 50%;
    background: linear-gradient(135deg, var(--lime), var(--lime-dark)); border: 2px solid var(--panel);
    box-shadow: 0 0 0 1.5px var(--lime); display: flex; align-items: center; justify-content: center; }
  .badge span { font-family: 'Oswald', sans-serif; font-weight: 700; color: #fff; font-size: 31px; line-height: 28px; text-align: center; transform: rotate(6deg); letter-spacing: 1px; }
  .badge-left { left: 410px; top: 847px; }
  .badge-right { left: 1048px; top: 143px; }

  .feature { position: absolute; left: 624px; font-family: 'Open Sans', sans-serif; font-size: 12px; line-height: 15.6px; color: var(--ink); }
  .feature-title { font-family: 'Oswald', sans-serif; font-size: 22px; line-height: 23px; color: var(--lime); }
  .feature-title strong { font-weight: 700; display: block; }
  .feature-title span { font-weight: 300; display: block; }
  .rule { width: 101px; height: 3px; background: var(--grey); margin: 10px 0 12px; }
  .feature-protein { top: 222px; }
  .feature-natural { top: 867px; width: 130px; }
  .feature-natural .rule { margin-top: 0; }
  .feature-natural b { position: absolute; left: 73px; top: 45px; font-size: 13px; line-height: 15.6px; }

  .product-band { position: absolute; left: 624px; top: 676px; width: 407px; height: 136px; background: var(--green); border-radius: 6px 0 0 6px; }
  .product-name { position: absolute; left: 25px; top: 26px; font-family: 'Oswald', sans-serif; font-size: 60px; line-height: 1; color: #fff; letter-spacing: -1px; white-space: nowrap; }
  .product-name .light { font-weight: 300; }
  .product-name .bold { font-weight: 700; }
  .natural-strip { position: absolute; left: 1033px; top: 676px; width: 37px; height: 136px; background: var(--green); display: flex; align-items: center; justify-content: center; }
  .natural-strip span { writing-mode: vertical-rl; font-family: 'Montserrat', sans-serif; font-weight: 700; font-size: 12.5px; color: #fff; }

  .tape-note { position: absolute; left: 838px; top: 52px; width: 175px; height: 20px; }
  .tape-note span { position: absolute; left: 10px; top: 5px; font-family: 'Oswald', sans-serif; font-weight: 500; font-size: 6.5px; color: var(--ink); white-space: nowrap; }
</style>
</head>
<body>
<div class="canvas">
  <div class="bag"></div>
  <div class="fold-v" style="left:70px"></div>
  <div class="fold-v" style="left:391px"></div>
  <div class="fold-v" style="left:543px"></div>
  <div class="fold-v" style="left:1031px"></div>
  <div class="fold-h" style="top:92px"></div>
  <div class="fold-h" style="top:989px"></div>

  <div class="illustration plant-left" role="img" aria-label="Faint line illustration of a soybean plant with leaves and pods"></div>
  <div class="illustration plant-right" role="img" aria-label="Faint line illustration of a soybean plant with leaves and pod"></div>

  <div class="tape-note">
    <svg width="175" height="20" viewBox="0 0 175 20" aria-hidden="true">
      <path d="M2 6 L6 12 L2 18 M6 12 H155 Q165 12 170 4 M160 3 L170 4 L168 12" fill="none" stroke="#1a1a1a" stroke-width="1"/>
    </svg>
    <span>E-Z OPEN-Hold Wide Tape... PULL NARROW TAPE</span>
  </div>

  <div class="brand brand-left">
    <div class="brand-mark"></div>
    <div class="brand-name">TRU-VORA</div>
  </div>

  <div class="info-band">
    <p>Lorem ipsum dolor sit amet, consec-<br>tetuer adipiscing elit, sed diam nonummy<br>nibh euismod tincidunt ut laoreet dolore<br>magna aliquam erat volutpat. Ut wisi<br>enim ad minim veniam, quis nostrud</p>
  </div>

  <div class="badge badge-left"><span>FARM<br>FRESH</span></div>
  <div class="badge badge-right"><span>FARM<br>FRESH</span></div>

  <div class="feature feature-protein">
    <div class="feature-title"><strong>PROTEIN</strong><span>SOURCE</span></div>
    <div class="rule"></div>
    <p>Lorem ipsum<br>dolor sit amet,<br>consectetuer</p>
  </div>

  <div class="brand brand-right">
    <div class="brand-mark"></div>
    <div class="brand-name">TRU-VORA</div>
  </div>

  <div class="product-band">
    <div class="product-name"><span class="light">SOYBEAN</span> <span class="bold">SEED</span></div>
  </div>
  <div class="natural-strip"><span>100% NATURAL</span></div>

  <div class="feature feature-natural">
    <div class="rule"></div>
    <p>Lorem ipsum<br>dolor sit amet,<br>consectetuer</p>
    <b>100%</b>
  </div>

  <div class="illustration beans" role="img" aria-label="Photo of two green soybean seeds"></div>
</div>
</body>
</html>
```